Business Cards - Brightwell Harbor

need to design unique business card for my mortgage business. I need to design credit card style business card for my business or any unique idea that you might have

Target Market(s)

Home Loan customers

Industry/Entity Type

Mortgage Brokerage

Contact Information for Business Card

please design credit card style or very unique style business card

Colors

Designer to choose colors to be used in the design.

Requirements
Must have
• Name
• position
• Phone number
• fax number
• email address
• website address
• social media address
• All above fields will be provided once design in finalised

```html
<!DOCTYPE html>
<html lang="en">
<head>
<meta charset="utf-8">
<title>Brightwell Harbor – Business Card</title>
<link rel="stylesheet" href="https://fonts.googleapis.com/css2?family=Saira:wght@400;600&family=Saira+Semi+Condensed:wght@600;700&display=swap">
<style>
  :root {
    --backdrop: #edd5a4;
    --card-top: #3d3731;
    --card-bottom: #2a2521;
    --ink-light: #f4f1ec;
    --ink-soft: #d9d4cc;
    --mark-blue: #4a66d6;
    --chip-light: #e9c77a;
    --chip-dark: #b98a3c;
    --chip-line: #8a6428;
  }
  * { box-sizing: border-box; margin: 0; padding: 0; }
  html, body {
    width: 1200px;
    height: 1200px;
    overflow: hidden;
    background: var(--backdrop);
  }
  .canvas {
    position: relative;
    width: 1200px;
    height: 1200px;
  }
  .card {
    position: absolute;
    left: 290px;
    width: 620px;
    height: 391px;
    border-radius: 22px;
    background: linear-gradient(160deg, var(--card-top), var(--card-bottom));
    overflow: hidden;
  }
  .card--front { top: 130px; }
  .card--back  { top: 680px; }

  /* Front */
  .front-wordmark {
    position: absolute;
    inset: 0;
    display: flex;
    align-items: center;
    justify-content: center;
    font-family: "Saira", sans-serif;
    font-weight: 400;
    font-size: 52px;
    letter-spacing: 1px;
    color: var(--ink-light);
    text-transform: uppercase;
  }

  /* Back */
  .label {
    position: absolute;
    font-family: "Saira Semi Condensed", sans-serif;
    font-weight: 700;
    font-size: 13px;
    letter-spacing: 0.5px;
    text-transform: uppercase;
    color: var(--ink-soft);
    white-space: nowrap;
  }
  .label--website { left: 92px;  top: 110px; }
  .label--fax     { left: 222px; top: 136px; }
  .label--social  { left: 420px; top: 236px; }
  .label--email   { left: 416px; top: 256px; }
  .label--phone   { left: 428px; top: 340px; font-size: 15px; color: var(--ink-light); }

  .holder-name {
    position: absolute;
    left: 78px;
    top: 190px;
    font-family: "Saira", sans-serif;
    font-weight: 400;
    font-size: 34px;
    color: var(--ink-soft);
  }
  .holder-position {
    position: absolute;
    left: 196px;
    top: 206px;
    font-family: "Saira Semi Condensed", sans-serif;
    font-weight: 700;
    font-size: 21px;
    letter-spacing: 0.5px;
    color: var(--ink-light);
    text-transform: uppercase;
  }
  .back-wordmark {
    position: absolute;
    left: 448px;
    top: 292px;
    width: 110px;
    font-family: "Saira", sans-serif;
    font-weight: 600;
    font-size: 13px;
    line-height: 1.1;
    text-align: center;
    color: var(--mark-blue);
    text-transform: uppercase;
  }
  .chip {
    position: absolute;
    left: 500px;
    top: 92px;
    width: 92px;
    height: 68px;
  }
</style>
</head>
<body>
  <main class="canvas">
    <section class="card card--front" aria-label="Card front">
      <div class="front-wordmark">Brightwell Harbor</div>
    </section>

    <section class="card card--back" aria-label="Card back">
      <span class="label label--website">Website Address</span>
      <span class="label label--fax">Fax Number</span>

      <span class="holder-name">Name</span>
      <span class="holder-position">Position</span>

      <svg class="chip" viewBox="0 0 92 68" aria-hidden="true">
        <defs>
          <linearGradient id="chipGold" x1="0" y1="0" x2="1" y2="1">
            <stop offset="0" stop-color="var(--chip-light)"/>
            <stop offset="1" stop-color="var(--chip-dark)"/>
          </linearGradient>
        </defs>
        <rect x="1" y="1" width="90" height="66" rx="10" fill="url(#chipGold)" stroke="var(--chip-line)" stroke-width="1.5"/>
        <g fill="none" stroke="var(--chip-line)" stroke-width="1.5">
          <rect x="32" y="18" width="28" height="32" rx="6"/>
          <line x1="1" y1="23" x2="32" y2="23"/>
          <line x1="1" y1="45" x2="32" y2="45"/>
          <line x1="60" y1="23" x2="91" y2="23"/>
          <line x1="60" y1="45" x2="91" y2="45"/>
          <line x1="46" y1="1" x2="46" y2="18"/>
          <line x1="46" y1="50" x2="46" y2="67"/>
        </g>
      </svg>

      <span class="label label--social">Social Media Address</span>
      <span class="label label--email">Email Address</span>

      <div class="back-wordmark">Brightwell Harbor</div>

      <span class="label label--phone">Phone Number</span>
    </section>
  </main>
</body>
</html>
```